Brochure Design for Marketing Firm in Melbourne

We are a boutique growth marketing firm based in Melbourne, Australia called Brindle Harbor Partners. We are a team of marketing and branding specialists who invest in marketing for businesses who exhibit strong growth potential and work collaboratively to achieve this.

Our business has a number of capabilities which we call the "Product Tool Suite". We utilise these product tools to grow our client's businesses through customer acquisition, sales, media investment etc. We require a designer to develop 13 brochures in line with the Brindle Harbor Partners Branding and colour palette.

The tools are listed below:
1. Brand Archetype Tool
2. Brand Audit Tool
3. Business Canvas
4. Call Centre Performance Tool
5. Communication Messaging Tool
6. Growth Audit Tool
7. Loyalty Program
8. Media Leverage Program
9. Product Optimisation Tool
10. Referral Tool
11. Sales Coaching/Training Tool
12. Segmentation Tool
13. Social Media Process

In order to select a designer, we invite designers to produce a mock up of one Tool in a brochure layout. Once we have chosen the winning design we will contract the designer to produce the remaining 12 brochures using that design.

Ideally we would like to each brochure to be 2 pages (back and front) but we understand that some tools may require 3 or 4 pages.

Please refer to the files that we have uploaded containing
- our logo
- copy (text)
- a PDF of our own attempt (please refer to this for design inspiration, they are photoshop compatible)
- Accompanying visuals (graphs, photos logos etc.)

The final design should communicate financial growth and our corporate identity. The style should have a professional and modern feel that is clean and crisp.

Target Market(s)

Our clients include businesses with a proven track record looking for further marketing investment to grow their business

Industry/Entity Type

Investment

Requirements
Must have
• The designs must feature:

- The Brindle Harbor Partners logo
- The Brindle Harbor Lantern
- Content (this is text combined with graphs and flowcharts which we have provided)

Please refer to the pdf uploaded to see the suggested design approach.

```html
<!DOCTYPE html>
<html lang="en">
<head>
<meta charset="utf-8">
<title>Brindle Harbor Partners – Product Tool Suite Covers</title>
<link href="https://fonts.googleapis.com/css2?family=Oswald:wght@500;600&family=Montserrat:wght@400;600&display=swap" rel="stylesheet">
<style>
  :root {
    --board: #9aa1a7;
    --ink-dark: #2c2d32;
    --paper: #e5e5e7;
    --brand-blue: #1d4f7c;
    --brand-sky: #27a6df;
    --text-grey: #8a8b8f;
    --c-cyan: #1ea8e0;
    --c-orange: #f39200;
    --c-lime: #8cc43f;
    --c-grey: #6c6d71;
    --c-purple: #7e5c8e;
    --c-olive: #6a7a4f;
    --c-blue: #2e6aa2;
    --c-green: #25a84a;
    --c-magenta: #c4238a;
    --c-teal: #3dbdb5;
    --c-yellow: #e2b419;
    --c-crimson: #a5173f;
    --c-flame: #f06a22;
  }
  * { box-sizing: border-box; margin: 0; padding: 0; }
  html, body { width: 808px; height: 1200px; overflow: hidden; background: var(--board); }
  .board { position: relative; width: 800px; height: 1188px; transform: scale(1.01); transform-origin: 0 0; }
  .defs { position: absolute; width: 0; height: 0; }

  .cover { position: absolute; width: 164px; height: 232px; background: var(--ink-dark); overflow: hidden; }
  .cover-art { position: absolute; inset: 0; width: 100%; height: 100%; }
  .paper { fill: var(--paper); }
  .photo { fill: url(#skyline); }
  .accent-band { fill: var(--accent); opacity: .85; }

  .cover-title { position: absolute; left: 3px; top: 8px; font: 600 14px/15px "Oswald", sans-serif; text-transform: uppercase; color: #fff; letter-spacing: .2px; }
  .cover-title span { display: block; width: fit-content; background: var(--accent); padding: 0 3px 0 7px; margin-bottom: 1px; }

  .brand { display: flex; align-items: center; gap: 3px; font: 600 8px/1 "Montserrat", sans-serif; color: var(--brand-blue); white-space: nowrap; }
  .brand::after { content: ""; width: 6px; height: 6px; background: var(--brand-sky); }
  .cover .brand { position: absolute; right: 10px; top: 207px; }

  .open-cover { position: absolute; left: 226px; top: 758px; width: 542px; height: 382px; background: var(--ink-dark); overflow: hidden; --accent: var(--c-crimson); }
  .open-cover .cover-title { left: 271px; top: 12px; font-size: 27px; line-height: 29px; }
  .open-cover .cover-title span { padding: 0 5px 0 16px; margin-bottom: 2px; }
  .spine { stroke: #c9c9cc; stroke-width: .5; }
  .connect { position: absolute; left: 14px; top: 236px; font: 500 8px/1 "Oswald", sans-serif; color: #fff; letter-spacing: .3px; text-transform: uppercase; }
  .back-brand { position: absolute; left: 14px; top: 276px; }
  .tagline { font: 400 5px/1 "Montserrat", sans-serif; color: #555; margin-top: 3px; }
  .front-brand { position: absolute; right: 22px; top: 330px; text-align: right; }
  .front-brand .brand { font-size: 12px; }
  .front-brand .brand::after { width: 9px; height: 9px; }
  .offices { position: absolute; left: 14px; top: 334px; display: flex; gap: 10px; font: 400 4.6px/6px "Montserrat", sans-serif; color: var(--text-grey); }
  .office + .office { border-left: 1px solid #bcbcc0; padding-left: 10px; }
  .office strong { display: block; font-weight: 600; color: #6a6b6f; }
  .social { position: absolute; left: 213px; top: 358px; display: flex; gap: 2px; }
  .social span { width: 7px; height: 7px; background: var(--c-blue); }
  .social span:nth-child(2) { background: var(--brand-blue); }
  .social span:nth-child(3) { background: var(--brand-sky); }
  .social span:nth-child(4) { background: #4a90c8; }
  .board-label { position: absolute; left: 0; width: 1000px; top: 1153px; left: 0; text-align: center; width: 1005px; font: 600 11px/1 "Montserrat", sans-serif; color: #fff; letter-spacing: .3px; }
</style>
</head>
<body>
<div class="board">
  <svg class="defs" aria-hidden="true">
    <defs>
      <linearGradient id="skyline" x1="0" y1="0" x2="0" y2="1">
        <stop offset="0" stop-color="#dcdcd9"/>
        <stop offset=".45" stop-color="#a9aaa8"/>
        <stop offset=".58" stop-color="#7b7e82"/>
        <stop offset="1" stop-color="#3b3e44"/>
      </linearGradient>
    </defs>
  </svg>

  <article class="cover" style="--accent:var(--c-cyan);left:37px;top:25px">
    <svg class="cover-art" viewBox="0 0 164 232"><rect class="paper" y="153" width="164" height="79"/><polygon class="photo" role="img" aria-label="Photo: businessman walking a tightrope above a city skyline" points="0,67 150,67 110,178 0,178"/><polygon class="accent-band" points="134,67 150,67 110,178 94,178"/></svg>
    <h2 class="cover-title"><span>Brand</span><span>Archetype</span><span>Tool</span></h2>
    <div class="brand">Brindle Harbor Partners</div>
  </article>
  <article class="cover" style="--accent:var(--c-orange);left:225px;top:25px">
    <svg class="cover-art" viewBox="0 0 164 232"><rect class="paper" y="153" width="164" height="79"/><polygon class="photo" role="img" aria-label="Photo: businessman walking a tightrope above a city skyline" points="0,67 150,67 110,178 0,178"/><polygon class="accent-band" points="134,67 150,67 110,178 94,178"/></svg>
    <h2 class="cover-title"><span>Brand</span><span>Audit</span><span>Tool</span></h2>
    <div class="brand">Brindle Harbor Partners</div>
  </article>
  <article class="cover" style="--accent:var(--c-lime);left:413px;top:25px">
    <svg class="cover-art" viewBox="0 0 164 232"><rect class="paper" y="153" width="164" height="79"/><polygon class="photo" role="img" aria-label="Photo: businessman walking a tightrope above a city skyline" points="0,67 150,67 110,178 0,178"/><polygon class="accent-band" points="134,67 150,67 110,178 94,178"/></svg>
    <h2 class="cover-title"><span>Business</span><span>Canvas</span><span>Tool</span></h2>
    <div class="brand">Brindle Harbor Partners</div>
  </article>
  <article class="cover" style="--accent:var(--c-grey);left:603px;top:25px">
    <svg class="cover-art" viewBox="0 0 164 232"><rect class="paper" y="153" width="164" height="79"/><polygon class="photo" role="img" aria-label="Photo: businessman walking a tightrope above a city skyline" points="0,67 150,67 110,178 0,178"/><polygon class="accent-band" points="134,67 150,67 110,178 94,178"/></svg>
    <h2 class="cover-title"><span>Social</span><span>Media</span><span>Process</span></h2>
    <div class="brand">Brindle Harbor Partners</div>
  </article>

  <article class="cover" style="--accent:var(--c-purple);left:37px;top:267px">
    <svg class="cover-art" viewBox="0 0 164 232"><rect class="paper" y="153" width="164" height="79"/><polygon class="photo" role="img" aria-label="Photo: businessman walking a tightrope above a city skyline" points="0,67 150,67 110,178 0,178"/><polygon class="accent-band" points="134,67 150,67 110,178 94,178"/></svg>
    <h2 class="cover-title"><span>Referral</span><span>Tool</span></h2>
    <div class="brand">Brindle Harbor Partners</div>
  </article>
  <article class="cover" style="--accent:var(--c-olive);left:225px;top:267px">
    <svg class="cover-art" viewBox="0 0 164 232"><rect class="paper" y="153" width="164" height="79"/><polygon class="photo" role="img" aria-label="Photo: businessman walking a tightrope above a city skyline" points="0,67 150,67 110,178 0,178"/><polygon class="accent-band" points="134,67 150,67 110,178 94,178"/></svg>
    <h2 class="cover-title"><span>Sales</span><span>Coaching/Training</span><span>Tool</span></h2>
    <div class="brand">Brindle Harbor Partners</div>
  </article>
  <article class="cover" style="--accent:var(--c-blue);left:413px;top:267px">
    <svg class="cover-art" viewBox="0 0 164 232"><rect class="paper" y="153" width="164" height="79"/><polygon class="photo" role="img" aria-label="Photo: businessman walking a tightrope above a city skyline" points="0,67 150,67 110,178 0,178"/><polygon class="accent-band" points="134,67 150,67 110,178 94,178"/></svg>
    <h2 class="cover-title"><span>Segmentation</span><span>Tool</span></h2>
    <div class="brand">Brindle Harbor Partners</div>
  </article>
  <article class="cover" style="--accent:var(--c-green);left:603px;top:267px">
    <svg class="cover-art" viewBox="0 0 164 232"><rect class="paper" y="153" width="164" height="79"/><polygon class="photo" role="img" aria-label="Photo: businessman walking a tightrope above a city skyline" points="0,67 150,67 110,178 0,178"/><polygon class="accent-band" points="134,67 150,67 110,178 94,178"/></svg>
    <h2 class="cover-title"><span>Growth</span><span>Audit</span><span>Tool</span></h2>
    <div class="brand">Brindle Harbor Partners</div>
  </article>

  <article class="cover" style="--accent:var(--c-magenta);left:37px;top:509px">
    <svg class="cover-art" viewBox="0 0 164 232"><rect class="paper" y="153" width="164" height="79"/><polygon class="photo" role="img" aria-label="Photo: businessman walking a tightrope above a city skyline" points="0,67 150,67 110,178 0,178"/><polygon class="accent-band" points="134,67 150,67 110,178 94,178"/></svg>
    <h2 class="cover-title"><span>Call Centre</span><span>Performance</span><span>Tool</span></h2>
    <div class="brand">Brindle Harbor Partners</div>
  </article>
  <article class="cover" style="--accent:var(--c-teal);left:225px;top:509px">
    <svg class="cover-art" viewBox="0 0 164 232"><rect class="paper" y="153" width="164" height="79"/><polygon class="photo" role="img" aria-label="Photo: businessman walking a tightrope above a city skyline" points="0,67 150,67 110,178 0,178"/><polygon class="accent-band" points="134,67 150,67 110,178 94,178"/></svg>
    <h2 class="cover-title"><span>Communication</span><span>Messaging</span><span>Tool</span></h2>
    <div class="brand">Brindle Harbor Partners</div>
  </article>
  <article class="cover" style="--accent:var(--c-yellow);left:413px;top:509px">
    <svg class="cover-art" viewBox="0 0 164 232"><rect class="paper" y="153" width="164" height="79"/><polygon class="photo" role="img" aria-label="Photo: businessman walking a tightrope above a city skyline" points="0,67 150,67 110,178 0,178"/><polygon class="accent-band" points="134,67 150,67 110,178 94,178"/></svg>
    <h2 class="cover-title"><span>Product</span><span>Optimisation</span><span>Tool</span></h2>
    <div class="brand">Brindle Harbor Partners</div>
  </article>
  <article class="cover" style="--accent:var(--c-crimson);left:603px;top:509px">
    <svg class="cover-art" viewBox="0 0 164 232"><rect class="paper" y="153" width="164" height="79"/><polygon class="photo" role="img" aria-label="Photo: businessman walking a tightrope above a city skyline" points="0,67 150,67 110,178 0,178"/><polygon class="accent-band" points="134,67 150,67 110,178 94,178"/></svg>
    <h2 class="cover-title"><span>Loyalty</span><span>Program</span><span>Tool</span></h2>
    <div class="brand">Brindle Harbor Partners</div>
  </article>

  <article class="cover" style="--accent:var(--c-flame);left:37px;top:757px">
    <svg class="cover-art" viewBox="0 0 164 232"><rect class="paper" y="153" width="164" height="79"/><polygon class="photo" role="img" aria-label="Photo: businessman walking a tightrope above a city skyline" points="0,67 150,67 110,178 0,178"/><polygon class="accent-band" points="134,67 150,67 110,178 94,178"/></svg>
    <h2 class="cover-title"><span>Media</span><span>Leverage</span><span>Program</span></h2>
    <div class="brand">Brindle Harbor Partners</div>
  </article>

  <section class="open-cover">
    <svg class="cover-art" viewBox="0 0 542 382">
      <rect class="paper" y="262" width="542" height="120"/>
      <polygon class="photo" role="img" aria-label="Photo: city skyline and sky continuing across the back cover" points="209,107 271,107 271,294 124,294"/>
      <polygon class="accent-band" points="209,107 227,107 142,294 124,294"/>
      <polygon class="photo" role="img" aria-label="Photo: businessman walking a tightrope above a city skyline" points="271,107 514,107 474,294 271,294"/>
      <polygon class="accent-band" points="496,107 514,107 474,294 456,294"/>
      <line class="spine" x1="271" y1="0" x2="271" y2="382"/>
    </svg>
    <h1 class="cover-title"><span>Loyalty</span><span>Program</span><span>Tool</span></h1>
    <p class="connect">Connect with us</p>
    <div class="back-brand">
      <div class="brand">Brindle Harbor Partners</div>
      <p class="tagline">"A Unique Approach to Growth"</p>
    </div>
    <div class="offices">
      <div class="office"><strong>Singapore Office:</strong>18 Kestrel Lane, #04-09,<br>Singapore, 000000<br>hello@brindleharbor.example</div>
      <div class="office"><strong>Melbourne Office:</strong>Level 4, 210 Fernhill Road<br>+61 3 9000 0000<br>team@brindleharbor.example</div>
    </div>
    <div class="social"><span></span><span></span><span></span><span></span></div>
    <div class="front-brand">
      <div class="brand">Brindle Harbor Partners</div>
      <p class="tagline">"A Unique Approach to Growth"</p>
    </div>
  </section>

  <p class="board-label">Open Cover</p>
</div>
</body>
</html>
```